Gestaltung von Plakaten für Bereich der Qualitätssicherung
Zielgruppe
Wir sind Betreiber von zwei MERUFA Märkten.
Aufgabenstellung
Das Plakat dient zur internen Verwendung und soll anfallende Aufgaben im Bereich der Qualitätssicherung zeigen.
Es gibt die Marktleitung und 4 Abteilungen. In diesen 5 Bereichen fallen wiederkehrende Aufgaben in verschiedenen Zeitfenstern an.
Es soll herausstechen, dass die Marktleitung für die anderen 4 Abteilungen verantwortlich ist. (Organigramm)
Bitte fügen Sie zu jeden der 5 Zuständigkeitsbereiche eine freie Zeile hinzu. (Verantwortlich im Markt: __________)
Im Anhang habe ich eine Word Datei mit allen Abteilungen und deren Aufgaben und eine grobe Skizze hinzugefügt.
Überschrift des Plakats: Qualitätssicherung im Markt
Die Gestaltung soll einfach aber hochwertig wirken. Nicht verspielt. Weißer oder schlichter Hintergrund.
Das Ziel ist durch das Plakat eine Übersicht zu schaffen, wer für welche Aufgaben wann verantwortlich ist.
Wichtig ist das der Rhythmus (Wann muss es erledigt werden) am Plakat deutlich zu sehen ist.
Bitte fügen Sie das angehängte MERUFA Logo hinzu, dezent rechts unten im Eck.
In die Fußzeile bitte: BLT Abschlussprojekt von Jonas Kreibl, MERUFA Kreibl in Lindenfeld
Wenn möglich bitte mit wenig kostenpflichtigen Stockmaterial.
Ich bin gespannt auf die Vorschläge.
Besten Dank im Voraus.

```html
<!DOCTYPE html>
<html lang="de">
<head>
<meta charset="utf-8">
<title>Qualitätssicherung im Markt</title>
<link rel="stylesheet" href="https://fonts.googleapis.com/css2?family=Montserrat:wght@400;500;600;700&display=swap">
<style>
  :root {
    --blue: #1a5ba6;
    --ink: #2b2b2b;
    --legend-bg: #dcdcdc;
    --c-monat: #c8202e;
    --c-quartal: #e8501e;
    --c-jahr: #f39200;
    --c-taeglich: #95c11f;
    --c-woche: #e2dc00;
    --c-bedarf: #35a9e1;
    --c-lieferung: #96237e;
    --white: #ffffff;
  }
  * { box-sizing: border-box; margin: 0; padding: 0; }
  html, body { width: 1200px; height: 801px; overflow: hidden; background: var(--white); }
  body { font-family: "Montserrat", sans-serif; color: var(--ink); }
  .poster { position: relative; width: 1200px; height: 801px; background: var(--white); }

  .title { position: absolute; left: 55px; top: 36px; font-size: 45px; font-weight: 700; color: var(--blue); letter-spacing: 0.2px; }

  .badge { display: inline-flex; align-items: center; justify-content: center; width: 26px; height: 26px; color: var(--white); font-size: 13.5px; font-weight: 500; flex: none; }
  .badge.m { background: var(--c-monat); }
  .badge.q { background: var(--c-quartal); }
  .badge.j { background: var(--c-jahr); }
  .badge.t { background: var(--c-taeglich); }
  .badge.w { background: var(--c-woche); color: var(--ink); }
  .badge.b { background: var(--c-bedarf); }
  .badge.l { background: var(--c-lieferung); }

  .legend-heading { position: absolute; left: 1030px; top: 36px; font-size: 15px; font-weight: 600; color: var(--ink); }
  .legend { position: absolute; left: 997px; top: 63px; width: 203px; height: 286px; background: var(--legend-bg); padding: 16px 0 0 30px; list-style: none; }
  .legend li { display: flex; align-items: center; gap: 12px; height: 36.2px; font-size: 16px; font-weight: 500; }

  .lead-box { position: absolute; left: 41px; top: 126px; width: 224px; height: 63px; background: var(--blue); color: var(--white); font-size: 26px; font-weight: 700; display: flex; align-items: center; justify-content: center; }
  .lead-label { position: absolute; left: 95px; top: 278px; width: 110px; text-align: center; font-size: 14.5px; font-weight: 500; line-height: 18px; color: var(--blue); background: var(--white); }

  .lead-tasks { position: absolute; left: 321px; top: 123px; list-style: none; }
  .lead-tasks li { display: flex; align-items: center; gap: 16px; height: 31.8px; font-size: 17.2px; }

  .connectors { position: absolute; left: 0; top: 0; }

  .dept { position: absolute; top: 420px; width: 255px; }
  .dept-name { height: 56px; border: 1.5px solid var(--blue); color: var(--blue); font-size: 27px; font-weight: 700; display: flex; align-items: center; justify-content: center; }
  .dept-tasks { list-style: none; margin-top: 21px; }
  .dept-tasks li { display: flex; align-items: center; gap: 11px; height: 58.6px; font-size: 17.2px; line-height: 20.5px; white-space: nowrap; }
  .dept-tasks li .badge { width: 25px; height: 25px; }
  .owner { position: absolute; top: 283px; left: 2px; font-size: 21.5px; white-space: nowrap; }
  .owner span { display: inline-block; width: 106px; border-bottom: 1.5px solid var(--ink); margin-left: 5px; }

  .footer { position: absolute; left: 0; bottom: 0; width: 1200px; height: 46px; background: var(--blue); color: var(--white); }
  .footer-text { position: absolute; right: 82px; top: 14px; font-size: 15px; font-weight: 500; }
  .brand { position: absolute; right: 12px; top: 14px; font-size: 15px; font-weight: 700; color: var(--white); }
</style>
</head>
<body>
<main class="poster">
  <h1 class="title">Qualitätssicherung im Markt</h1>

  <div class="legend-heading">LEGENDE</div>
  <ul class="legend">
    <li><span class="badge m">M</span>1x Monat</li>
    <li><span class="badge q">Q</span>1x Quartal</li>
    <li><span class="badge j">J</span>1x Quartal</li>
    <li><span class="badge t">T</span>täglich</li>
    <li><span class="badge w">W</span>wöchentlich</li>
    <li><span class="badge b">B</span>nach Bedarf</li>
    <li><span class="badge l">L</span>pro Lieferung</li>
  </ul>

  <svg class="connectors" width="1200" height="801" viewBox="0 0 1200 801" aria-hidden="true">
    <g stroke="#1a5ba6" stroke-width="2" fill="none">
      <line x1="150" y1="189" x2="150" y2="413"/>
      <line x1="150" y1="394" x2="1072" y2="394"/>
      <line x1="468" y1="394" x2="468" y2="413"/>
      <line x1="774" y1="394" x2="774" y2="413"/>
      <line x1="1072" y1="394" x2="1072" y2="413"/>
      <line x1="313" y1="424" x2="313" y2="737"/>
      <line x1="619" y1="428" x2="619" y2="741"/>
      <line x1="916" y1="428" x2="916" y2="741"/>
    </g>
    <g fill="#1a5ba6">
      <polygon points="145,412 155,412 150,420"/>
      <polygon points="463,412 473,412 468,420"/>
      <polygon points="769,412 779,412 774,420"/>
      <polygon points="1067,412 1077,412 1072,420"/>
    </g>
  </svg>

  <div class="lead-box">Marktleitung</div>
  <div class="lead-label">verantwortlich für</div>

  <ul class="lead-tasks">
    <li><span class="badge m">M</span>Temperaturkontrolle aller Truhen</li>
    <li><span class="badge q">Q</span>Marktbegehung</li>
    <li><span class="badge j">J</span>Hygieneschulung</li>
    <li><span class="badge j">J</span>Mitarbeiterbelehrung Infektionsschutzgesetz</li>
    <li><span class="badge j">J</span>Kontrolle QHR- Ware</li>
    <li><span class="badge b">B</span>Dokumentation der Verantwortlichkeiten</li>
    <li><span class="badge b">B</span>Ablage Nachweisdokumente Schädlingsbekämpfung</li>
    <li><span class="badge b">B</span>Dokumentation und Ablage Warenrückruf</li>
  </ul>

  <section class="dept" style="left:31px">
    <div class="dept-name">Obst &amp; Gemüse</div>
    <ul class="dept-tasks">
      <li><span class="badge t">T</span>Dokumentation<br>Wareneingangskontrolle</li>
      <li><span class="badge t">T</span>Temperaturkontrolle<br>steckerfertige Truhen</li>
      <li><span class="badge t">T</span>Kennzeichnung<br>„behandelte Ware“</li>
    </ul>
    <div class="owner">Verantwortl.:<span></span></div>
  </section>

  <section class="dept" style="left:339px">
    <div class="dept-name">MoPro</div>
    <ul class="dept-tasks">
      <li><span class="badge t">T</span>Dokumentation<br>Wareneingangskontrolle</li>
      <li><span class="badge t">T</span>Temperaturkontrolle<br>steckerfertige Truhen</li>
      <li><span class="badge t">T</span>MHD- Qualitätskontrolle<br>während der Lagerung</li>
    </ul>
    <div class="owner">Verantwortl.:<span></span></div>
  </section>

  <section class="dept" style="left:643px">
    <div class="dept-name">Tiefkühl</div>
    <ul class="dept-tasks">
      <li><span class="badge l">L</span>Dokumentation<br>Wareneingangskontrolle</li>
      <li><span class="badge w">W</span>MHD- Qualitätskontrolle<br>während der Lagerung</li>
    </ul>
    <div class="owner">Verantwortl.:<span></span></div>
  </section>

  <section class="dept" style="left:932px">
    <div class="dept-name">Lebensmittel</div>
    <ul class="dept-tasks">
      <li><span class="badge w">W</span>MHD- Qualitätskontrolle<br>während der Lagerung</li>
    </ul>
    <div class="owner">Verantwortl.:<span></span></div>
  </section>

  <footer class="footer">
    <div class="footer-text">BLT Abschlussprojekt von Jonas Kreibl, MERUFA Kreibl in Lindenfeld</div>
    <div class="brand">MERUFA</div>
  </footer>
</main>
</body>
</html>
```